Homecare Design. I would like the color to be same as my business cards

Velvet Homemaker & Companion Agency
I would something very light on the eyes.
Easy to read nothing complicated
I want something that demonstrate soft touch
Updates

My contact number has change cell: 415-555-0188 office: 4155550142

Target Market(s)

Elderly
people looking for someone to take care of there love ones
Target age starting at 50

Industry/Entity Type

Business

Font styles to use
Serif

Colors
3176b5
3276b5
85acd3
ceddec

Requirements

Nice to have
• I woluld like something like helping hands
Should not have
• I really don't care to see medical supplies, medication

```html
<!DOCTYPE html>
<html lang="en">
<head>
<meta charset="utf-8">
<title>Velvet Homemaker &amp; Companion Agency – Postcard</title>
<link href="https://fonts.googleapis.com/css2?family=Lato:wght@400;700;900&family=Libre+Baskerville:wght@700&family=Roboto+Condensed:wght@500&display=swap" rel="stylesheet">
<style>
  :root {
    --page-bg: #5f6264;
    --blue: #3176b5;
    --blue-dark: #25609a;
    --blue-mid: #85acd3;
    --blue-pale: #ceddec;
    --ink: #2a2e33;
    --body-ink: #3a3a3a;
    --paper: #ffffff;
  }
  * { box-sizing: border-box; margin: 0; padding: 0; }
  html, body { width: 900px; height: 1200px; overflow: hidden; }
  body { background: var(--page-bg); position: relative; font-family: "Lato", sans-serif; }

  .card { position: absolute; left: 100px; width: 695px; height: 538px; background: var(--paper); overflow: hidden; box-shadow: 0 4px 14px rgba(0,0,0,.35); }
  .card--front { top: 37px; }
  .card--back { top: 605px; background: linear-gradient(90deg, #ffffff 0%, #ececec 55%, #dcdcdc 75%, #ffffff 100%); }

  /* Front */
  .family-photo { position: absolute; left: 0; top: 0; width: 695px; height: 440px;
    background: radial-gradient(ellipse at 50% 45%, #d9c7bb 0%, #b8b4c2 35%, #8e97b0 60%, #e8e2de 100%); }
  .front-shapes { position: absolute; inset: 0; }
  .call-box { position: absolute; left: 55px; top: 258px; width: 220px; height: 176px; border: 4px solid #f4f4f4; border-radius: 18px;
    background: linear-gradient(180deg, var(--blue-mid) 0%, var(--blue) 55%, var(--blue-dark) 100%);
    box-shadow: 0 3px 8px rgba(0,0,0,.35); text-align: center; padding-top: 18px; }
  .call-box__lead { font-weight: 700; font-size: 43px; line-height: 43px; color: var(--ink); }
  .call-box__phone { font-family: "Roboto Condensed", sans-serif; font-weight: 500; font-size: 30px; color: #fff; margin-top: 8px; letter-spacing: .5px; }
  .name-band { position: absolute; left: 0; top: 463px; width: 695px; height: 46px;
    background: linear-gradient(180deg, var(--blue-pale), var(--blue-mid)); border-top: 2px solid #fff; border-bottom: 2px solid #fff;
    font-family: "Libre Baskerville", serif; font-weight: 700; font-size: 19.5px; color: #1b2633;
    display: flex; align-items: center; justify-content: center; letter-spacing: .3px; }
  .name-band__strip { position: absolute; left: 0; top: 509px; width: 695px; height: 29px; background: linear-gradient(180deg,#e6e6e6,#f7f7f7); }

  /* Back */
  .back-shapes { position: absolute; inset: 0; }
  .stamp-box { position: absolute; left: 590px; top: 82px; width: 75px; height: 89px; border: 1.5px solid #222; background: #fff; }
  .address-line { position: absolute; left: 490px; width: 176px; height: 2px; background: #222; }
  .section-title { position: absolute; left: 19px; color: var(--blue); font-weight: 700; font-size: 23.5px; letter-spacing: .3px; }
  .about-text { position: absolute; left: 20px; top: 55px; width: 385px; font-size: 15.6px; line-height: 20.8px; color: var(--body-ink); }
  .service-list { position: absolute; list-style: none; font-weight: 700; font-size: 16.5px; line-height: 21px; color: var(--body-ink); }
  .service-list li { position: relative; padding-left: 20px; margin-bottom: 8px; }
  .service-list li::before { content: ""; position: absolute; left: 0; top: 6px; width: 10px; height: 10px; border-radius: 50%;
    background: var(--blue-mid); border: 1.5px solid var(--blue-dark); }
  .service-list--left { left: 21px; top: 225px; }
  .service-list--right { left: 206px; top: 225px; }
  .hours { position: absolute; left: 45px; top: 380px; width: 330px; height: 91px; border-radius: 22px 0 0 22px;
    background: linear-gradient(90deg, var(--blue-dark) 0%, var(--blue) 55%, var(--blue-mid) 100%);
    border: 3px solid #f2f2f2; border-right: none; padding: 9px 30px 0 0; text-align: right; font-weight: 700; font-size: 16px; line-height: 22px; }
  .hours__day { color: var(--blue-pale); }
  .hours__time { color: #ffffff; }
  .web-address { position: absolute; left: 20px; top: 490px; font-weight: 700; font-size: 15.5px; color: #222; }
</style>
</head>
<body>

<section class="card card--front">
  <div class="family-photo" role="img" aria-label="Photo of a smiling grandmother embracing two young grandchildren holding a teddy bear"></div>
  <svg class="front-shapes" width="695" height="538" viewBox="0 0 695 538" aria-hidden="true">
    <defs>
      <linearGradient id="frontWhite" x1="0" y1="0" x2="0" y2="1">
        <stop offset="0" stop-color="#ffffff"/><stop offset="1" stop-color="#e9e9e9"/>
      </linearGradient>
    </defs>
    <path d="M0,290 C40,300 70,310 120,325 L0,345 Z" fill="var(--blue)"/>
    <path d="M0,318 C200,385 420,430 600,420 C640,416 670,405 695,392 L695,538 L0,538 Z" fill="url(#frontWhite)"/>
    <path d="M480,425 C570,418 640,395 695,350 L695,372 C640,408 570,428 480,425 Z" fill="var(--blue)"/>
  </svg>
  <div class="call-box">
    <div class="call-box__lead">CALL US<br>TODAY</div>
    <div class="call-box__phone">415-555-0188</div>
  </div>
  <div class="name-band">VELVET HOMEMAKER &amp; COMPANION AGENCY</div>
  <div class="name-band__strip"></div>
</section>

<section class="card card--back">
  <svg class="back-shapes" width="695" height="538" viewBox="0 0 695 538" aria-hidden="true">
    <defs>
      <linearGradient id="backBlue" x1="0" y1="0" x2="0" y2="1">
        <stop offset="0" stop-color="#3176b5"/><stop offset=".5" stop-color="#85acd3"/><stop offset="1" stop-color="#ceddec"/>
      </linearGradient>
    </defs>
    <path d="M440,0 C500,60 495,200 430,330 C385,430 400,500 450,538" fill="none" stroke="url(#backBlue)" stroke-width="50"/>
    <path d="M458,0 C515,60 510,200 445,330 C400,430 415,500 465,538 L695,538 L695,0 Z" fill="#ffffff"/>
  </svg>

  <h2 class="section-title" style="top:18px">ABOUT&nbsp; US</h2>
  <p class="about-text">Velvet Homemaker &amp; Companion Agency, assist elderly clients who need assistance in or out of the home. Our home care services to our clients to assist them to lead dignified&nbsp; and independent lives in the comfort and safety of there own homes</p>

  <h2 class="section-title" style="top:183px">OUR SERVICES</h2>
  <ul class="service-list service-list--left">
    <li>Assistance with<br>daily living</li>
    <li>Companionship</li>
    <li>Light Cooking</li>
    <li>Laundry</li>
  </ul>
  <ul class="service-list service-list--right">
    <li>Run errands</li>
    <li>Doctors visits</li>
    <li>light House keeping</li>
    <li>In and out of<br>home activities</li>
  </ul>

  <div class="hours">
    <div><span class="hours__day">MONDAY - FRIDAY:</span> <span class="hours__time">8:00 - 5:00 PM.</span></div>
    <div><span class="hours__day">SATURDAY:</span> <span class="hours__time">8:00 - 2:00 PM.</span></div>
    <div><span class="hours__day">SUNDAY:</span> <span class="hours__time">CLOSED</span></div>
  </div>

  <div class="web-address">www.velvethomemakerandcompanion.com</div>

  <div class="stamp-box"></div>
  <div class="address-line" style="top:286px"></div>
  <div class="address-line" style="top:314px"></div>
  <div class="address-line" style="top:343px"></div>
</section>

</body>
</html>
```